Package of web graphics needed

Utilizing a recently selected logo from a Pixel Harbor contest, we need to have some ads, fb cover, home page slide image created for our new 844-Toll-Free Number Product. Please feel free to check our site at www.ringvantagehub.com

You'll find attached the 844 toll free logo in 2 layouts.

Here are the ads and dimensions of each that are needed:
1.)Banners/ads - 468x60
468×60 px
125×125 px
120×600 px
120x90 px
88×31 px button
5.)FB Cover - 851 x 315
6.)Home page slider image - 944 x 328

Here is the text & some ideas to use for these. Feel free to use different versions depending on which ad they work better on:
-

Market Your Business in a Memorable Way – Pre-Order Yours Today, Deadline: Dec. 7th
[include logo]
-
[844 logo] Don't Miss out on your chance to finally get a great vanity!

Order Yours Today
-

Don't Miss out on your chance to finally get a great vanity!
Dec. 7th Deadline to pre-order

Don't Ignore 844!– The newest toll free prefix – Coming Dec. 7th – Get Yours Today

FB COVER guidelines -
Requirements:
Include the logo
Limited Time Left – Get your Reservation in by December 7th

HOME PAGE Image Slide:
Use the logo,

Couple of Ideas we're interested in seeing:

[Billboard sign stock image … with the number 877-Grab-ONE on the billboard]
[844 logo and caricature] [1 caricature looking surprised]

```html
<!DOCTYPE html>
<html lang="en">
<head>
<meta charset="utf-8">
<title>RingVantage 844 Web Ad Package</title>
<link rel="stylesheet" href="https://fonts.googleapis.com/css2?family=Montserrat:wght@400;500;700;800&family=PT+Sans+Narrow:wght@400;700&display=swap">
<style>
:root{
  --board:#2b2b29;
  --navy:#0f3466;
  --navy-deep:#0a2a57;
  --green:#5cb531;
  --green-light:#b9e07f;
  --green-pale:#e3f3c6;
  --grey-text:#6b6b6b;
  --white:#ffffff;
  --sky:#1e7fd6;
  --sky-light:#8fd0f7;
}
*{box-sizing:border-box;margin:0;padding:0}
html,body{width:1200px;height:962px;overflow:hidden;background:var(--board)}
.board{position:relative;width:1200px;height:962px;font-family:"PT Sans Narrow",Arial,sans-serif}
.ad{position:absolute;overflow:hidden}
.brand{font-weight:700;color:var(--navy);white-space:nowrap;line-height:1}

/* 125x125 */
.ad-square{left:192px;top:87px;width:125px;height:125px;background:linear-gradient(180deg,var(--green-pale),var(--green-light));text-align:center}
.ad-square .brand{font-size:22px;margin-top:14px}
.ad-square .copy{color:var(--navy);font-size:15px;line-height:18px;margin-top:20px}
.ad-square .band{position:absolute;left:0;bottom:0;width:100%;height:29px;background:var(--navy);color:var(--white);font-weight:700;font-size:15px;line-height:29px}

/* 120x90 */
.ad-small{left:336px;top:122px;width:120px;height:90px;background:linear-gradient(180deg,var(--green-pale),var(--green-light));text-align:center}
.ad-small .brand{font-size:20px;margin-top:10px}
.ad-small .copy{color:var(--navy);font-size:14px;margin-top:16px}
.ad-small .band{position:absolute;left:0;bottom:0;width:100%;height:21px;background:var(--navy);color:var(--white);font-weight:700;font-size:12px;line-height:21px}

/* 88x31 */
.ad-button{left:493px;top:91px;width:88px;height:31px;background:var(--green-light);display:flex;align-items:center;justify-content:center}
.ad-button .brand{font-size:14px}

/* 468x60 */
.ad-leader{left:485px;top:152px;width:468px;height:60px;background:var(--white);border:1px solid #d8e6cd}
.ad-leader .brand{position:absolute;left:10px;top:20px;font-size:20px}
.ad-leader .swoosh{position:absolute;left:160px;top:0;width:308px;height:60px}
.ad-leader .copy{position:absolute;left:196px;top:10px;color:var(--navy);font-size:14.5px;line-height:19px}
.ad-leader .cta{position:absolute;left:397px;top:3px;width:61px;height:53px;background:var(--navy);color:var(--white);font-size:13.5px;line-height:15px;text-align:center;padding-top:4px;border:1px solid #6f8fb8}

/* 120x600 */
.ad-sky{left:1027px;top:91px;width:120px;height:600px;background:linear-gradient(180deg,#eaf6d5 20%,var(--green-light));font-family:"Montserrat",Arial,sans-serif}
.ad-sky .head{height:120px;background:var(--white);text-align:center;padding-top:40px}
.ad-sky .head .brand{font-family:"PT Sans Narrow",Arial,sans-serif;font-size:24px}
.ad-sky .curve{position:absolute;left:0;top:108px;width:120px;height:30px}
.ad-sky .copy{position:absolute;left:11px;top:152px;color:var(--navy);font-size:16px;font-weight:500;line-height:24px}
.ad-sky .deadline{position:absolute;left:11px;top:333px;color:var(--navy);font-size:15px;line-height:24px}
.ad-sky .deadline .date{font-size:19px}
.ad-sky .cta{position:absolute;left:11px;top:464px;width:99px;height:88px;background:var(--navy);color:var(--white);font-family:"PT Sans Narrow",Arial,sans-serif;font-weight:700;font-size:23px;line-height:24px;text-align:center;padding-top:7px;border-radius:3px}

/* FB cover */
.ad-cover{left:50px;top:244px;width:851px;height:315px;font-family:"Montserrat",Arial,sans-serif}
.ad-cover .waves{position:absolute;inset:0;background:
  radial-gradient(ellipse 70% 45% at 55% 95%,rgba(30,140,220,.55),transparent 70%),
  radial-gradient(ellipse 40% 60% at 95% 20%,rgba(92,181,49,.5),transparent 70%),
  linear-gradient(160deg,#ffffff 40%,#cfeaf6 70%,#4fb6d8 100%)}
.ad-cover .brand{position:absolute;left:30px;top:35px;font-size:38px;font-weight:800;font-family:"Montserrat",Arial,sans-serif}
.ad-cover .tagline{position:absolute;left:377px;top:35px;color:var(--grey-text);font-size:21px;line-height:27px;font-weight:400}
.ad-cover .limited{position:absolute;left:59px;top:156px;color:var(--navy);font-size:22px;letter-spacing:2.5px}
.ad-cover .reserve{position:absolute;left:380px;top:135px;width:273px;height:66px;background:var(--green);color:var(--white);font-size:20px;line-height:27px;padding:6px 0 0 19px;border-left:2px solid var(--green)}
.ad-cover .reserve sup{font-size:11px}

/* Home slider */
.ad-slider{left:50px;top:589px;width:944px;height:328px;font-family:"Montserrat",Arial,sans-serif}
.ad-slider .scene{position:absolute;inset:0;background:linear-gradient(180deg,var(--sky-light) 0%,var(--sky) 55%,#155fb0 100%)}
.ad-slider .sign{position:absolute;left:125px;top:40px;width:677px;height:228px;background:linear-gradient(180deg,#f4f5f6,#e3e6e9);border:3px solid #b9bec4}
.ad-slider .sign-logo{position:absolute;left:25px;top:41px;width:414px;height:144px;background:var(--white);display:flex;align-items:center;justify-content:center}
.ad-slider .sign-logo .brand{font-size:54px;font-weight:800;font-family:"Montserrat",Arial,sans-serif}
.ad-slider .call{position:absolute;left:460px;top:48px;font-weight:800;font-size:64px;line-height:68px}
.ad-slider .call .l1{color:var(--navy);display:block}
.ad-slider .call .l2{color:var(--green);display:block}
</style>
</head>
<body>
<main class="board">

  <section class="ad ad-square" aria-label="125 by 125 ad">
    <div class="brand">RingVantage</div>
    <p class="copy">The newest<br>TOLL FREE prefix</p>
    <div class="band">Coming Dec. 7<sup>th</sup></div>
  </section>

  <section class="ad ad-small" aria-label="120 by 90 ad">
    <div class="brand">RingVantage</div>
    <p class="copy">TOLL FREE prefix</p>
    <div class="band">Coming Dec. 7th</div>
  </section>

  <section class="ad ad-button" aria-label="88 by 31 button">
    <div class="brand">RingVantage</div>
  </section>

  <section class="ad ad-leader" aria-label="468 by 60 banner">
    <div class="brand">RingVantage</div>
    <svg class="swoosh" viewBox="0 0 308 60" aria-hidden="true">
      <defs><linearGradient id="leaderGreen" x1="0" x2="1"><stop offset="0" stop-color="#cdeaa0"/><stop offset="1" stop-color="#9dd25c"/></linearGradient></defs>
      <path d="M22 0 H308 V60 H0 C14 40 16 12 22 0Z" fill="url(#leaderGreen)"/>
      <path d="M22 0 C16 12 14 40 0 60 H8 C20 40 22 14 30 0Z" fill="var(--green)"/>
    </svg>
    <p class="copy">Don't Miss out on your chance<br>to finally get a great vanity!</p>
    <div class="cta">ORDER<br>YOURS<br>TODAY</div>
  </section>

  <section class="ad ad-sky" aria-label="120 by 600 skyscraper">
    <div class="head"><div class="brand">RingVantage</div></div>
    <svg class="curve" viewBox="0 0 120 30" aria-hidden="true">
      <path d="M0 4 C40 14 80 16 120 12 V18 C80 22 40 22 0 10Z" fill="var(--navy)"/>
    </svg>
    <p class="copy">Don't Miss<br>out on your<br>chance to<br>finally get<br>a great<br>vanity!</p>
    <p class="deadline"><span class="date">DEC. 7<sup>th</sup></span><br>Deadline to<br>pre-order</p>
    <div class="cta">ORDER<br>YOURS<br>TODAY</div>
  </section>

  <section class="ad ad-cover" aria-label="Facebook cover">
    <div class="waves" role="img" aria-label="Flowing blue and green abstract light waves"></div>
    <div class="brand">RingVantage</div>
    <p class="tagline">Don't Miss out on your chance<br>to finally get a great vanity!</p>
    <p class="limited">LIMITED TIME LEFT</p>
    <div class="reserve">Get your Reservation<br>in by DECEMBER 7<sup>th</sup></div>
  </section>

  <section class="ad ad-slider" aria-label="Home page slider">
    <div class="scene" role="img" aria-label="Billboard on a highway in front of a blue city skyline"></div>
    <div class="sign">
      <div class="sign-logo"><div class="brand">RingVantage</div></div>
      <div class="call"><span class="l1">CALL</span><span class="l2">NOW</span></div>
    </div>
  </section>

</main>
</body>
</html>
```